New Tequila Alcohol Package Design

We are launching a new premium pre-made tequila jello shot product. We currently have a vodka jello 20 pack product. Please see our website and Instagram for current product:
https://blixshotsco.com/
https://www.snapgramly.com/blixshotsco/
PROJECT DETAILS:
Design a 4 pack jello shot box. Box similar to: https://shopcellarmavu.ca/products/curly-jellz-lucky-fox-4-x-30-ml
there will be one main image (top) and a front and back side (small). Please see the dimensions.
PLEASE SEE DESIGN TEMPLATE.
Dimensions are: 12.5cm*12.5cm*1.5cm
LOGO: BLIXshots Agave Gelatin Shots
FLAVOUR: Margarita Raspberry
DESIGN: We don't have a lot of directions for this. We are potentially looking for something completely different than what we already have, so please keep that in mind.
OUR BRAND: Fun, bold, colorful, outrageous. Needs to be eye-catching to be grabbed off of the shelf in a crowded liquor industry.
BLIX - it's gone. Reasoning for the brand. The brand is a bit of a "joke" and is not serious.
We have used fruit "emoji/vectors" in the background in the past.

We will require more than one design in the future (we already have more than one flavour ready to market). We are looking for a designer we can potentially work with on future projects.

Target Market(s)

18-29, more female/GenZ-focused.

Industry/Entity Type

alcohol

Font styles to use
Other font styles liked:
• Please choose for us. Ideally "MARGARITA" is the main focus.

Requirements
Must have
• Please see the Text Required Document

```html
<!DOCTYPE html>
<html lang="en">
<head>
<meta charset="utf-8">
<title>BLIXshots Margarita Raspberry – 4 pack lid</title>
<link rel="stylesheet" href="https://fonts.googleapis.com/css2?family=Fraunces:opsz,wght@144,900&family=Rubik:wght@800;900&family=Yellowtail&display=swap">
<style>
  :root {
    --bg: #f3f3f3;
    --lid-pink: #ec2a86;
    --hot-pink: #ff1a7a;
    --white: #ffffff;
    --ink: #111111;
    --berry: #d9479b;
  }
  html, body {
    margin: 0;
    width: 1200px;
    height: 1142px;
    overflow: hidden;
    background: var(--bg);
  }
  .lid {
    position: absolute;
    left: 200px;
    top: 171px;
    width: 800px;
    height: 800px;
    margin: 0;
    border-radius: 14px;
    background: var(--lid-pink);
    overflow: hidden;
    font-family: "Rubik", sans-serif;
  }
  .lid__glow {
    position: absolute;
    inset: 0;
    background:
      radial-gradient(circle at 30% 32%, rgba(245,210,26,.85) 0 8%, transparent 30%),
      radial-gradient(circle at 55% 28%, rgba(63,191,42,.9) 0 10%, transparent 32%),
      radial-gradient(circle at 28% 60%, rgba(240,138,28,.85) 0 10%, transparent 32%),
      radial-gradient(circle at 40% 72%, rgba(242,33,44,.85) 0 10%, transparent 30%),
      radial-gradient(circle at 62% 70%, rgba(63,191,42,.75) 0 8%, transparent 28%),
      radial-gradient(circle at 80% 35%, rgba(106,60,201,.7) 0 6%, transparent 26%),
      radial-gradient(circle at 78% 58%, rgba(40,70,140,.6) 0 6%, transparent 24%);
  }
  .brand {
    position: absolute;
    left: 150px;
    top: 60px;
    margin: 0;
  }
  .brand__name {
    font-weight: 900;
    font-size: 104px;
    line-height: 1;
    color: var(--white);
    letter-spacing: -1px;
    white-space: nowrap;
  }
  .brand__tagline {
    position: absolute;
    left: 165px;
    top: 185px;
    margin: 0;
    font-weight: 800;
    font-size: 20px;
    line-height: 1.15;
    letter-spacing: 2px;
    color: var(--ink);
  }
  .fruit-art {
    position: absolute;
    border-radius: 50%;
    background: radial-gradient(circle at 40% 40%, #f07ab9, var(--berry) 60%, #a82a6f);
  }
  .fruit-art--small { left: 640px; top: 190px; width: 130px; height: 100px; }
  .fruit-art--large { left: 470px; top: 270px; width: 170px; height: 130px; }
  .flavour {
    position: absolute;
    left: 0;
    right: 0;
    top: 410px;
    margin: 0;
    text-align: center;
  }
  .flavour__main {
    display: block;
    font-family: "Fraunces", serif;
    font-weight: 900;
    font-size: 120px;
    line-height: 1;
    color: var(--white);
    transform: rotate(8deg);
  }
  .flavour__sub {
    display: inline-block;
    margin-top: 0;
    font-weight: 900;
    font-size: 84px;
    line-height: 1;
    color: var(--hot-pink);
    -webkit-text-stroke: 3px var(--white);
    transform: rotate(8deg);
  }
  .spec {
    position: absolute;
    margin: 0;
    font-family: "Yellowtail", cursive;
    color: var(--white);
    font-size: 42px;
    line-height: 1;
    white-space: nowrap;
  }
  .spec--abv { left: 40px; top: 650px; transform: rotate(6deg); }
  .spec--volume { right: 60px; top: 700px; transform: rotate(6deg); }
</style>
</head>
<body>
  <main class="lid">
    <div class="lid__glow"></div>

    <p class="brand"><span class="brand__name">BLIXshots</span></p>
    <p class="brand__tagline">PREMIUM<br>AGAVE<br>GELATIN</p>

    <div class="fruit-art fruit-art--small" role="img" aria-label="Raspberry illustration"></div>
    <div class="fruit-art fruit-art--large" role="img" aria-label="Raspberry illustration"></div>

    <h1 class="flavour">
      <span class="flavour__main">Margarita</span>
      <span class="flavour__sub">Raspberry</span>
    </h1>

    <p class="spec spec--abv">12% alc./vol.</p>
    <p class="spec spec--volume">4x50ml</p>
  </main>
</body>
</html>
```